Medical IT Business with New logo needs a fresh stationary design

First time on sketch Harbor; Thought I would give it a go.
This project is for business cards alone but we have loads of design work that needs to take place in the immediate future.

We provide IT services to the Medical Industry and value ourselves as offering a premium product to the market.

I am after a fresh, clean design using full colour 2 sided cards which includes our current colour palettes from our logo.

Card's must include:
- Logo
- Slogan
- Name
- Adress
- Email
- Phone
- Fax
- Mobile

Target Market(s)

Surgeons, High Profile Medical Personnel

Industry/Entity Type

Business

Fonts, CMYK Colours and Logo files attached.

Requirements
Must have
• Card's must include:
• - Logo
• - Slogan
• - Name
• - Adress
• - Email
• - Phone
• - Fax
• - Mobile
Nice to have
• Needs to incorporate our colour palette (attached CMYK colours)
Should not have
• Black backgrounds. Black text ok.

```html
<!DOCTYPE html>
<html lang="en">
<head>
<meta charset="utf-8">
<title>Carevault Systems – Business Cards</title>
<link href="https://fonts.googleapis.com/css2?family=Open+Sans:wght@400;600;700&display=swap" rel="stylesheet">
<style>
  :root {
    --navy: #113a73;
    --blue: #0b7fb6;
    --sky: #4fa6d8;
    --slogan: #8a9bb5;
    --white: #ffffff;
    --backdrop: #e6e8ec;
  }
  * { margin: 0; padding: 0; box-sizing: border-box; }
  html, body {
    width: 1200px; height: 900px; overflow: hidden;
    background: var(--backdrop);
    font-family: "Open Sans", Arial, sans-serif;
  }
  .canvas { position: relative; width: 1200px; height: 900px; }

  .card {
    position: absolute; width: 600px; height: 343px;
    border-radius: 18px; overflow: hidden;
    box-shadow: 0 14px 30px rgba(17, 58, 115, 0.18);
  }

  /* Front card */
  .card--front { left: 90px; top: 80px; background: var(--navy); }
  .front-lockup {
    position: absolute; left: 150px; top: 108px;
    display: flex; align-items: center; gap: 22px;
  }
  .brand-dot {
    width: 104px; height: 104px; border-radius: 50%;
    background: var(--blue); flex: none;
  }
  .brand-name {
    font-weight: 700; font-size: 40px; line-height: 1.0;
    color: var(--white); letter-spacing: 1px;
  }
  .front-lockup .slogan { color: var(--sky); font-size: 15px; margin-top: 8px; }

  /* Back card */
  .card--back { left: 510px; top: 470px; background: var(--white); }
  .back-art { position: absolute; inset: 0; }
  .back-brand { position: absolute; left: 44px; top: 100px; }
  .back-brand .brand-name { color: var(--navy); font-size: 34px; }
  .slogan { color: var(--slogan); font-size: 14px; margin-top: 6px; }

  .holder { position: absolute; left: 0; top: 218px; }
  .holder-name {
    display: flex; align-items: center; gap: 12px;
    font-weight: 700; font-size: 20px; color: var(--navy); letter-spacing: 0.5px;
  }
  .holder-name::before {
    content: ""; width: 32px; height: 4px; background: var(--blue);
  }
  .holder-address {
    margin-left: 44px; margin-top: 6px;
    color: var(--blue); font-size: 15px; line-height: 1.35;
  }

  .contact-list {
    position: absolute; right: 28px; top: 168px;
    list-style: none; text-align: right;
    color: var(--white); font-size: 14px; line-height: 1.55;
  }
  .contact-list li { display: flex; justify-content: flex-end; align-items: center; gap: 10px; }
  .contact-list svg { width: 13px; height: 13px; flex: none; }
  .contact-list .email { margin-top: 6px; }
</style>
</head>
<body>
<main class="canvas">

  <section class="card card--front" aria-label="Business card front">
    <div class="front-lockup">
      <span class="brand-dot"></span>
      <div>
        <div class="brand-name">CAREVAULT<br>SYSTEMS</div>
        <div class="slogan">secure IT for your clinic</div>
      </div>
    </div>
  </section>

  <section class="card card--back" aria-label="Business card back">
    <svg class="back-art" viewBox="0 0 600 343" preserveAspectRatio="none" aria-hidden="true">
      <line x1="420" y1="52" x2="600" y2="52" stroke="#0b7fb6" stroke-width="12"/>
      <path d="M380,120 C330,220 300,300 150,343 L600,343 L600,60 L440,60 Z" fill="#113a73"/>
      <path d="M372,118 C322,218 292,296 140,343" fill="none" stroke="#0b7fb6" stroke-width="8"/>
      <path d="M362,116 C312,214 280,290 128,343" fill="none" stroke="#ffffff" stroke-width="4"/>
      <path d="M0,300 C60,318 110,326 150,343 L0,343 Z" fill="#0b7fb6"/>
      <path d="M0,312 C70,330 130,336 180,343" fill="none" stroke="#113a73" stroke-width="10"/>
      <circle cx="420" cy="88" r="72" fill="#0b7fb6" stroke="#ffffff" stroke-width="4"/>
    </svg>

    <div class="back-brand">
      <div class="brand-name">CAREVAULT<br>SYSTEMS</div>
      <div class="slogan">secure IT for your clinic</div>
    </div>

    <div class="holder">
      <div class="holder-name">MARTEN ELLIS</div>
      <div class="holder-address">48 Harbour Lane<br>Fairview, NY 10410</div>
    </div>

    <ul class="contact-list">
      <li>+330 4815-2093
        <svg viewBox="0 0 16 16" aria-label="Phone"><path d="M3 1l3 3-2 2c1 2 3 4 5 5l2-2 3 3-2 2C7 14 2 9 1 3z" fill="#fff"/></svg></li>
      <li>+330 4815-2094
        <svg viewBox="0 0 16 16" aria-label="Fax"><rect x="4" y="1" width="8" height="5" fill="none" stroke="#fff" stroke-width="1.5"/><rect x="1" y="6" width="14" height="7" rx="1" fill="#fff"/></svg></li>
      <li>+330 6172-3381
        <svg viewBox="0 0 16 16" aria-label="Mobile"><rect x="4" y="1" width="8" height="14" rx="1.5" fill="none" stroke="#fff" stroke-width="1.5"/><circle cx="8" cy="12.5" r="1" fill="#fff"/></svg></li>
      <li class="email">info@carevaultsystems.com
        <svg viewBox="0 0 16 16" aria-label="Email"><rect x="1" y="3" width="14" height="10" fill="none" stroke="#fff" stroke-width="1.5"/><path d="M1 3l7 6 7-6" fill="none" stroke="#fff" stroke-width="1.5"/></svg></li>
    </ul>
  </section>

</main>
</body>
</html>
```